Brightwell Korrin Dental Practice Anniversary Flyer

Letter Box Drop Flyer (DL size)

We need a flyer design for letterbox drop. On the occasion of our practice anniversary in march 2014 we want to offer our patients special discounts.

1, vexa teeth whitening for 699$ (usually costs 1200$)
2. 10 percent discount on all Dental treatments like Orthavue, Pelbrook set, Crowns and Bridges, Mouthguards and Implants.

Attached Brightwell Korrin logo.

```html
<!DOCTYPE html>
<html lang="en">
<head>
<meta charset="utf-8">
<title>Brightwell Korrin Dental Practice – Anniversary Flyer</title>
<link rel="stylesheet" href="https://fonts.googleapis.com/css2?family=Archivo+Black&family=Archivo+Narrow:wght@500;700&display=swap">
<style>
  :root {
    --green-deep: #4f8a17;
    --green-mid: #7cb53a;
    --green-light: #a9d46b;
    --green-rule: #5d8c24;
    --offer-green: #b9e27a;
    --price-edge: #1f3a08;
    --white: #ffffff;
    --yellow: #fff23a;
    --ink: #1b1b1b;
    --paper: #ffffff;
  }
  html, body {
    margin: 0;
    padding: 0;
    overflow: hidden;
    background: var(--paper);
  }
  .flyer {
    position: relative;
    width: 1200px;
    height: 2180px;
    overflow: hidden;
    background: var(--paper);
    font-family: "Archivo Narrow", "Arial Narrow", sans-serif;
  }
  .offer-panel {
    position: absolute;
    inset: 0 0 auto 0;
    height: 1668px;
    background:
      linear-gradient(120deg, transparent 0 30%, rgba(255,255,255,.12) 30% 38%, transparent 38% 55%, rgba(255,255,255,.10) 55% 60%, transparent 60%),
      radial-gradient(ellipse at 50% 40%, var(--green-light) 0%, var(--green-mid) 45%, var(--green-deep) 100%);
  }
  .offer-panel > * {
    position: absolute;
    left: 0;
    right: 0;
    margin: 0;
    text-align: center;
  }
  .headline {
    top: 60px;
    font-family: "Archivo Black", sans-serif;
    font-size: 134px;
    line-height: 160px;
    color: var(--white);
    text-shadow: 0 0 6px #000, 4px 4px 0 #000, -2px -2px 0 #000;
  }
  .price {
    top: 470px;
    font-family: "Archivo Black", sans-serif;
    color: var(--offer-green);
    -webkit-text-stroke: 3px var(--price-edge);
    text-shadow: 5px 5px 0 var(--price-edge), 0 0 10px rgba(0,0,0,.6);
    line-height: 180px;
  }
  .price .for { font-size: 118px; }
  .price .amount { font-size: 170px; }
  .was-price, .discount {
    font-weight: 700;
    color: var(--yellow);
    text-shadow: 0 0 5px #000, 3px 3px 0 #000;
  }
  .was-price { top: 686px; font-size: 76px; line-height: 84px; }
  .discount { top: 808px; font-size: 92px; line-height: 96px; }
  .treatments {
    top: 1018px;
    list-style: none;
    padding: 0;
    font-weight: 500;
    font-size: 104px;
    line-height: 116px;
    color: var(--white);
    text-shadow: 0 0 5px #000, 3px 3px 0 #000;
  }
  .divider {
    position: absolute;
    left: 0; right: 0;
    top: 1690px;
    height: 12px;
    background: var(--green-rule);
  }
  .brand {
    position: absolute;
    left: 0; right: 0;
    top: 1920px;
    text-align: center;
  }
  .brand-name {
    display: inline-flex;
    align-items: center;
    gap: 24px;
    font-family: "Archivo Narrow", "Arial Narrow", sans-serif;
    font-weight: 700;
    font-size: 110px;
    line-height: 128px;
    color: var(--ink);
  }
  .brand-dot {
    width: 44px; height: 44px;
    border-radius: 50%;
    background: var(--green-mid);
  }
</style>
</head>
<body>
<main class="flyer">
  <section class="offer-panel">
    <h1 class="headline">Vexa teeth<br>whitening</h1>
    <p class="price"><span class="for">for </span><span class="amount">699$</span></p>
    <p class="was-price">(usually costs 1200$)</p>
    <p class="discount">10 percent discount on all<br>Dental treatments like</p>
    <ul class="treatments">
      <li>Orthavue</li>
      <li>Pelbrook set</li>
      <li>Crowns and Bridges</li>
      <li>Mouthguards</li>
      <li>and Implants.</li>
    </ul>
  </section>
  <div class="divider"></div>
  <footer class="brand">
    <div class="brand-name"><span class="brand-dot"></span>Brightwell Korrin</div>
  </footer>
</main>
</body>
</html>
```